Business card design needed for Marbury Medical Practice

We need a new design for our growing medical practice. Our previous design used blue, white and black. I would like to have a design with a baby, child, adult and grandparent on it. We look after a wide range of patients from newborns to 100 year olds.

Industry/Entity Type

Medical

Contact Information for Business Card

Marbury Medical Practice
14 Dunmore Rd Ridgevale, NSW 2794
Ph 4820 3647 Fax 4913 2506
Dr Helen Voss Dr Andrea Pollard
Dr Wendy Trelawny Dr Janice Whitworth
Dr Tom Ashbrook Dr Neil Dunn-Foster
Open Mon- Fri 9-1, 2-5pm
Sat 9-12pm by appointment
web:www.marburymedix.com.au
email:marburymedix@mailzonex.com

```html
<!DOCTYPE html>
<html lang="en">
<head>
<meta charset="utf-8">
<title>Marbury Medical Practice – Business Card</title>
<link rel="stylesheet" href="https://fonts.googleapis.com/css2?family=Arimo:wght@700&family=Didact+Gothic&display=swap">
<style>
  :root {
    --brand-blue: #2b4f93;
    --brand-blue-deep: #1f3d78;
    --card-white: #ffffff;
    --ink: #1d1d1d;
    --stage: #e9ebef;
    --slot-grey: #e6e8ec;
    --photo-a: #b9b2ad;
    --photo-b: #6f7f9c;
  }
  * { box-sizing: border-box; margin: 0; padding: 0; }
  html, body { width: 1200px; height: 900px; overflow: hidden; }
  body {
    background: var(--stage);
    font-family: "Didact Gothic", "Century Gothic", sans-serif;
    position: relative;
  }
  .card {
    position: absolute;
    left: 290px;
    width: 620px;
    height: 354px;
    background: var(--card-white);
    box-shadow: 0 10px 28px rgba(0,0,0,.22);
    overflow: hidden;
  }
  .card--front { top: 70px; }
  .card--back { top: 476px; background: var(--brand-blue); }
  .card__shapes { position: absolute; inset: 0; width: 100%; height: 100%; }

  .practice-title {
    position: absolute;
    font-family: "Arimo", Arial, sans-serif;
    font-weight: 700;
    letter-spacing: .2px;
    padding: 9px 0 9px 26px;
    border-top: 2px solid currentColor;
    border-bottom: 2px solid currentColor;
    white-space: nowrap;
  }
  .card--front .practice-title { top: 92px; left: 0; width: 262px; color: var(--card-white); font-size: 19px; }
  .card--back .practice-title { top: 48px; left: 0; width: 330px; color: var(--brand-blue); font-size: 22px; }

  .contact-lines {
    position: absolute;
    left: 40px; top: 178px;
    color: var(--card-white);
    font-size: 17px;
    line-height: 1.5;
    white-space: nowrap;
  }
  .contact-lines .phones span + span { margin-left: 22px; }
  .contact-lines .address { margin-top: 10px; padding-left: 80px; }

  .web-lines {
    position: absolute;
    left: 382px; top: 26px;
    color: var(--brand-blue);
    font-family: "Arimo", Arial, sans-serif;
    font-weight: 700;
    font-size: 13px;
    line-height: 1.35;
    white-space: nowrap;
  }
  .team-photo {
    position: absolute;
    left: 372px; top: 82px;
    width: 230px; height: 258px;
    background: linear-gradient(160deg, var(--photo-b), var(--photo-a) 60%, #d9cfc8);
  }

  .doctor-list {
    position: absolute;
    left: 40px; top: 168px;
    list-style: none;
    color: var(--ink);
    font-size: 19px;
    line-height: 1.32;
    white-space: nowrap;
  }
  .doctor-list li::before {
    content: "";
    display: inline-block;
    width: 7px; height: 7px;
    border-radius: 50%;
    background: var(--brand-blue);
    margin-right: 10px;
    vertical-align: middle;
  }

  .opening-hours {
    position: absolute;
    left: 400px; top: 26px;
    width: 200px;
    text-align: center;
    color: var(--card-white);
    font-family: "Arimo", Arial, sans-serif;
    font-weight: 700;
    font-size: 16px;
    line-height: 1.4;
  }
  .opening-hours .label { margin-bottom: 12px; }

  .appointment-slot {
    position: absolute;
    left: 380px; top: 150px;
    width: 222px; height: 160px;
  }
  .appointment-slot__tab {
    position: absolute;
    left: 30px; top: 0;
    width: 192px; height: 34px;
    background: var(--slot-grey);
    border-radius: 8px 8px 0 0;
  }
  .appointment-slot__body {
    position: absolute;
    left: 0; top: 26px;
    width: 222px; height: 134px;
    background: var(--slot-grey);
    border-radius: 8px;
    padding: 0 18px;
  }
  .appointment-slot__label {
    position: absolute;
    left: 62px; top: 9px;
    color: var(--brand-blue);
    font-size: 13px;
    white-space: nowrap;
  }
  .appointment-slot__line {
    height: 28px;
    border-bottom: 1px solid var(--brand-blue);
  }
  .appointment-slot__line:first-child { height: 22px; }
</style>
</head>
<body>

  <section class="card card--front" aria-label="Business card front">
    <svg class="card__shapes" viewBox="0 0 620 354" aria-hidden="true">
      <path d="M0 0 H262 Q392 177 268 354 H0 Z" fill="var(--brand-blue)"/>
      <path d="M290 0 Q420 177 300 354 L314 354 Q436 177 306 0 Z" fill="var(--brand-blue)"/>
    </svg>
    <h1 class="practice-title">Marbury Medical Practice</h1>
    <div class="contact-lines">
      <p class="phones"><span>Ph 4820 3647</span><span>Fax 4913 2506</span></p>
      <p class="address">14 Dunmore Rd Ridgevale,<br>NSW 2794</p>
    </div>
    <div class="web-lines">
      <p>www.marburymedix.com.au</p>
      <p>marburymedix@mailzonex.com</p>
    </div>
    <div class="team-photo" role="img" aria-label="Group photo of a family spanning a baby, children, adults and grandparents"></div>
  </section>

  <section class="card card--back" aria-label="Business card back">
    <svg class="card__shapes" viewBox="0 0 620 354" aria-hidden="true">
      <path d="M0 0 H330 Q440 177 340 354 H0 Z" fill="var(--card-white)"/>
      <path d="M352 0 Q462 177 362 354 L376 354 Q478 177 368 0 Z" fill="var(--card-white)"/>
    </svg>
    <h2 class="practice-title">Marbury Medical Practice</h2>
    <ul class="doctor-list">
      <li>Dr Helen Voss</li>
      <li>Dr Andrea Pollard</li>
      <li>Dr Wendy Trelawny</li>
      <li>Dr Janice Whitworth</li>
      <li>Dr Tom Ashbrook</li>
      <li>Dr Neil Dunn-Foster</li>
    </ul>
    <div class="opening-hours">
      <p class="label">Open:</p>
      <p>Mon- Fri 9-1, 2-5pm</p>
      <p>Sat 9-12pm</p>
    </div>
    <div class="appointment-slot">
      <div class="appointment-slot__tab"></div>
      <div class="appointment-slot__body">
        <div class="appointment-slot__line"></div>
        <div class="appointment-slot__line"></div>
        <div class="appointment-slot__line"></div>
        <div class="appointment-slot__line"></div>
      </div>
      <p class="appointment-slot__label">Next appointment:</p>
    </div>
  </section>

</body>
</html>
```